Rw construct holdings pty ltd

This is a development and construction company. Website can be set up on our domain rwbuildgroup.net if we could change the domain to rwbuildgroup.com.au would be great

Want the page to have eye catching designs, red, black and white are the preffered colours.

Check out www.tolumine.com.au it is my former company with my partner which i am now venturing out on my own, that is the perfect example of the website i want even allot of the information would be the same

Industry/Entity Type

Construction

Coding

Coded - Design and coding required

Number of Pages Required

5+ page

Requirements
Must have
• Company logo eye catching designs

```html
<!DOCTYPE html>
<html lang="en">
<head>
<meta charset="utf-8">
<title>RW Construct — Development &amp; Construction</title>
<link href="https://fonts.googleapis.com/css2?family=Montserrat:ital,wght@0,400;0,500;0,600;0,700;1,400&display=swap" rel="stylesheet">
<style>
:root{
  --red:#e8411f;
  --red-deep:#b8260f;
  --ink:#1f1f1f;
  --text:#333333;
  --muted:#8a8a8a;
  --white:#ffffff;
  --line:#dcdcdc;
  --paper:#f4f4f4;
  --footer:#0d0d0d;
}
*{box-sizing:border-box;margin:0;padding:0}
html,body{width:1200px;height:4326px;overflow:hidden}
body{position:relative;font-family:"Montserrat",sans-serif;color:var(--text);background:var(--white)}
section,header,footer{position:absolute;left:0;width:1200px}
.abs{position:absolute}
.center{text-align:center;left:0;width:1200px}
.btn{position:absolute;background:var(--red);color:var(--white);font-size:15px;font-weight:600;letter-spacing:.8px;text-transform:uppercase;display:flex;align-items:center;justify-content:center}
.brand{position:absolute;display:flex;align-items:center;gap:12px;font-family:"Montserrat",sans-serif;font-weight:600;letter-spacing:3px;text-transform:uppercase;white-space:nowrap}
.brand .dot{width:12px;height:12px;background:var(--red)}

/* hero */
.hero{top:0;height:673px;overflow:hidden}
.hero-photo{position:absolute;inset:0;background:linear-gradient(180deg,#c9ccd6 0%,#a6a8ae 18%,#6f6c6b 45%,#4a3f3b 72%,#2d2624 100%)}
.hero .brand{left:160px;top:30px;font-size:27px;color:var(--ink)}
.nav{position:absolute;right:164px;top:38px;display:flex;gap:20px;font-size:13.5px;font-weight:500;letter-spacing:.4px;color:var(--ink)}
.nav .active{font-weight:700}
.hero h1{position:absolute;top:336px;font-size:33px;line-height:46px;font-weight:700;color:var(--white);letter-spacing:.5px;text-transform:uppercase;text-shadow:0 2px 6px rgba(0,0,0,.45)}
.hero .btn{left:498px;top:445px;width:203px;height:42px}
.hero .chev{position:absolute;left:589px;top:634px}

/* about */
.about{top:718px;height:512px;overflow:hidden}
.about-photo{position:absolute;inset:0;background:linear-gradient(90deg,#f3f3f3 0%,#fafafa 45%,#e9e9e9 75%,#dedede 100%)}
.about .label{top:52px;font-size:21px;font-weight:600;color:var(--red);letter-spacing:1px}
.about .brand{left:402px;top:87px;font-size:31px;color:var(--ink)}
.about .lead{top:146px;font-size:17px;line-height:29px;font-weight:600;color:var(--ink)}
.about .copy{font-size:13px;color:var(--text);line-height:24px}
.about .btn{left:532px;top:381px;width:136px;height:42px}

/* services */
.services{top:1230px;height:512px}
.service{position:absolute;top:0;width:600px;height:512px;overflow:hidden;color:var(--white)}
.service.construction{left:0;background:linear-gradient(135deg,#c8321a 0%,#b22612 55%,#9b1d0d 100%)}
.service.renovation{left:600px;background:linear-gradient(135deg,#2c2c2c 0%,#3a3836 50%,#1d1d1d 100%)}
.service .icon{position:absolute;left:160px;top:70px}
.service.renovation .icon{left:40px}
.service h3{position:absolute;left:160px;top:176px;font-size:26px;font-weight:600;letter-spacing:.6px}
.service p{position:absolute;left:162px;top:218px;width:400px;font-size:12.3px;line-height:21.6px;color:rgba(255,255,255,.9)}
.service.renovation h3,.service.renovation p{left:40px}
.service .plus{position:absolute;left:161px;top:394px;width:47px;height:46px;border:1.5px solid var(--white);display:flex;align-items:center;justify-content:center;font-size:24px;font-weight:400}
.service.renovation .plus{left:42px}

/* projects */
.projects{top:1742px;height:777px}
.projects h2{top:84px;font-size:30px;font-weight:600;color:var(--ink);letter-spacing:.5px}
.projects .sub{top:128px;font-size:14px;line-height:27px;color:var(--text)}
.project{position:absolute;top:216px;width:274px;height:381px}
.project .photo{position:absolute;left:0;top:0;width:274px;height:297px}
.project .card{position:absolute;left:17px;top:243px;width:240px;height:138px;background:var(--white);box-shadow:0 3px 10px rgba(0,0,0,.14);text-align:center;padding-top:14px}
.project h4{font-size:17.5px;font-weight:600;color:var(--ink);margin-bottom:6px}
.project p{font-size:11.5px;line-height:18.5px;color:var(--text);padding:0 14px}
.projects .btn{left:498px;top:642px;width:203px;height:44px}

/* quality */
.quality{top:2519px;height:412px;overflow:hidden}
.quality-photo{position:absolute;inset:0;background:linear-gradient(120deg,#1e232b 0%,#3a414b 45%,#2a3038 75%,#151a20 100%)}
.quality h2{top:100px;font-size:37px;font-weight:600;color:var(--white);letter-spacing:1.5px}
.quality p{top:152px;font-size:18.5px;line-height:32.5px;color:rgba(255,255,255,.92)}
.quality .btn{left:502px;top:276px;width:203px;height:44px}

/* reviews */
.reviews{top:2931px;height:588px;overflow:hidden}
.reviews h2{top:84px;font-size:30px;font-weight:600;color:var(--ink);letter-spacing:.5px}
.review-card{position:absolute;left:220px;top:172px;width:760px;height:315px;background:var(--white);box-shadow:0 2px 18px rgba(0,0,0,.1);text-align:center}
.review-card .quote{position:absolute;left:346px;top:41px}
.review-card blockquote{position:absolute;left:20px;top:137px;width:720px;font-style:italic;font-size:11.5px;line-height:23px;color:var(--text);white-space:nowrap}
.review-card .who{position:absolute;left:0;top:252px;width:760px;font-size:16px;font-weight:500;color:var(--red)}
.review-card .where{position:absolute;left:0;top:276px;width:760px;font-size:13.5px;color:var(--text)}
.side-review{position:absolute;font-style:italic;font-size:11.5px;line-height:22.6px;color:#a9a9a9;white-space:nowrap;overflow:hidden}
.side-review.left{left:0;top:226px;width:134px;text-align:right}
.side-review.right{left:1075px;top:236px;width:125px}
.arrow{position:absolute;top:297px;width:30px;height:61px;display:flex;align-items:center;justify-content:center}
.arrow.prev{left:213px;background:#e5e5e5}
.arrow.next{left:958px;background:var(--red)}

/* contact */
.contact{top:3519px;height:540px;background:var(--paper)}
.contact h2{top:66px;font-size:30px;font-weight:600;color:var(--ink);letter-spacing:.5px}
.field{position:absolute;background:var(--white);border:1px solid var(--line);font-size:12px;color:#444;padding:12px 14px}
.field.select::after{content:"";position:absolute;right:14px;top:19px;border-left:4px solid transparent;border-right:4px solid transparent;border-top:5px solid #333}
.contact .btn{left:510px;top:419px;width:180px;height:44px}

/* footer */
.site-footer{top:4059px;height:267px;background:var(--footer);color:var(--white)}
.site-footer .brand{left:160px;top:86px;font-size:24px;color:var(--white)}
.chip{position:absolute;top:91px;height:42px;display:flex;align-items:center;background:var(--white);color:var(--ink);font-size:13.5px;white-space:nowrap;overflow:hidden}
.chip .ico{flex:none;width:45px;height:42px;background:var(--red);display:flex;align-items:center;justify-content:center;margin-right:12px}
.social{position:absolute;top:91px;width:42px;height:42px;background:var(--red);display:flex;align-items:center;justify-content:center}
.social span{width:12px;height:12px;border:2px solid var(--white);border-radius:50%}
.rule{position:absolute;left:160px;top:186px;width:880px;height:1px;background:#3a3a3a}
.foot-links{position:absolute;left:163px;top:215px;display:flex;gap:28px;font-size:13.5px}
.copyright{position:absolute;right:163px;top:215px;font-size:13.5px}
</style>
</head>
<body>

<header class="hero">
  <div class="hero-photo" role="img" aria-label="Modern two-storey brick and rendered home at dusk with garage and balconies"></div>
  <div class="brand"><span>RW Construct</span><span class="dot"></span></div>
  <nav class="nav">
    <span class="active">HOME</span><span>ABOUT US</span><span>SERVICES</span><span>PROJECTS</span><span>CONTACT US</span>
  </nav>
  <h1 class="center">We are development and construction<br>company in Australia</h1>
  <div class="btn">Contact us today</div>
  <svg class="chev" width="22" height="22" viewBox="0 0 22 22" fill="none" stroke="#e8411f" stroke-width="2.4"><path d="M4 3l7 7 7-7"/><path d="M4 11l7 7 7-7"/></svg>
</header>

<section class="about">
  <div class="about-photo" role="img" aria-label="Faint sketch of a kitchen interior beside a builder in a hard hat seen from behind"></div>
  <div class="abs center label">ABOUT</div>
  <div class="brand"><span class="dot"></span><span>RW Construct</span></div>
  <div class="abs center lead">We At RW Construct Believe That Building Your Dream Home<br>Shouldn't Cost Your Life Savings!</div>
  <div class="abs center copy" style="top:220px">Nor should it take a lifetime to build!</div>
  <div class="abs center copy" style="top:251px">We are determined to make your new build your forever home!</div>
  <div class="abs center copy" style="top:282px">At RW Construct we have one goal: to create innovative designs and build quality homes, to suit all budgets.<br>A simple but powerful philosophy that typifies the way we do business. We believe that the quality of our service<br>can assist our clients to reduce their costs by getting it right the first time.</div>
  <div class="btn">Read more</div>
</section>

<section class="services">
  <div class="service construction" role="img" aria-label="Red-toned photo of a construction site with workers and building frames">
    <svg class="icon" width="76" height="76" viewBox="0 0 76 76" fill="none" stroke="#fff" stroke-width="2">
      <path d="M10 72V20h14v52M10 30h14M10 42h14M10 54h14"/>
      <path d="M17 20V6M4 10h60M17 6l40 4M40 10v14"/>
      <rect x="34" y="24" width="12" height="8"/>
      <path d="M32 72V44h36v28M32 52h36M32 62h36M44 44v28M56 44v28M2 72h72"/>
    </svg>
    <h3>CONSTRUCTION</h3>
    <p>Lorem Ipsum is simply dummy text of the printing typesetting industry. Lorem Ipsum has been the industry's standard dummy text ever since the 1500s, when an unknown printer type and scrambled it to make a type specimen book. It has survived not only five centuries, but also the leap into electronic typesetting, remaining essentially unchanged. It was popularised in the 1960s with the release of Tarvelle sheets containing</p>
    <div class="plus">+</div>
  </div>
  <div class="service renovation" role="img" aria-label="Dark photo of a renovated open-plan living room with sofa and kitchen">
    <svg class="icon" width="76" height="76" viewBox="0 0 76 76" fill="none" stroke="#fff" stroke-width="2.2">
      <circle cx="38" cy="38" r="28"/>
      <path d="M38 4v8M38 64v8M4 38h8M64 38h8M14 14l6 6M56 56l6 6M62 14l-6 6M20 56l-6 6"/>
      <path d="M24 38l14-12 14 12M28 35v15h20V35M34 50v-8h8v8"/>
    </svg>
    <h3>RENOVATION</h3>
    <p>Lorem Ipsum is simply dummy text of the printing typesetting industry. Lorem Ipsum has been the industry's standard dummy text ever since the 1500s, when an unknown printer type and scrambled it to make a type specimen book. It has survived not only five centuries, but also the leap into electronic typesetting, remaining essentially unchanged. It was popularised in the 1960s with the release of Tarvelle sheets containing</p>
    <div class="plus">+</div>
  </div>
</section>

<section class="projects">
  <h2 class="abs center">OUR PROJECTS</h2>
  <div class="abs center sub">Usce non tellus ut lectus imperdiet gravida. Morbi sit amet ipsum et ipsum ultrices<br>aliquet fusce vulputate lorem.</div>
  <article class="project" style="left:161px">
    <div class="photo" role="img" aria-label="Contemporary white and grey home facade under blue sky" style="background:linear-gradient(180deg,#5d86c2 0%,#a9bdd6 35%,#cfcfcf 60%,#8c8c8c 100%)"></div>
    <div class="card"><h4>Mauris Imperdiet</h4><p>Etiam luctus odio libero, ut vestibul dolor viverra sed. Sed ut erosgryyu aliquam, semper mi non, volutpatr erat ut sagittis ligula eget.</p></div>
  </article>
  <article class="project" style="left:463px">
    <div class="photo" role="img" aria-label="Bright living room with timber floating staircase and beige sofa" style="background:linear-gradient(180deg,#f2f2f0 0%,#d9d6d0 40%,#8f7c66 75%,#3f3832 100%)"></div>
    <div class="card"><h4>Donec Eu Sem</h4><p>Etiam luctus odio libero, ut vestibul dolor viverra sed. Sed ut erosgryyu aliquam, semper mi non, volutpatr erat ut sagittis ligula eget.</p></div>
  </article>
  <article class="project" style="left:765px">
    <div class="photo" role="img" aria-label="Building site with concrete slab reinforcement laid out" style="background:linear-gradient(180deg,#4f7fc0 0%,#9fb8d8 30%,#8b8478 55%,#c9b89d 100%)"></div>
    <div class="card"><h4>Praesent Sollicitudin</h4><p>Etiam luctus odio libero, ut vestibul dolor viverra sed. Sed ut erosgryyu aliquam, semper mi non, volutpatr erat ut sagittis ligula eget.</p></div>
  </article>
  <div class="btn">View all projects</div>
</section>

<section class="quality">
  <div class="quality-photo" role="img" aria-label="Dark view looking up at glass office towers"></div>
  <h2 class="abs center">QUALTIY, INNOVATION &amp; EXCELLENCE</h2>
  <p class="abs center">Our commitment to quality and excellence in home design has helped us become the<br>builders we are today. We've never been satisfied with simply building homes 'the way<br>it's always been done.' This is what sets our company apart from the rest.</p>
  <div class="btn">Contact us today</div>
</section>

<section class="reviews">
  <h2 class="abs center">CLIENT REVIEWS</h2>
  <div class="side-review left">printing and typesetting<br>the standard dummy text<br>printer took a galley of type<br>book. It has survived not<br>into electronic typesetting,<br>released in the 1960s with<br>Lorem Ipsum passages, and<br>tools like Quillset Layout<br>versions of Lorem Ipsum.</div>
  <div class="review-card">
    <svg class="quote" width="68" height="68" viewBox="0 0 68 68"><circle cx="34" cy="34" r="32" fill="none" stroke="#e8411f" stroke-width="2.5"/><circle cx="34" cy="34" r="26" fill="#e8411f"/><path d="M22 40a6 6 0 1 0 6-6c0-5 3-8 7-9v-3c-7 1-13 7-13 18zM36 40a6 6 0 1 0 6-6c0-5 3-8 7-9v-3c-7 1-13 7-13 18z" fill="#fff"/></svg>
    <blockquote>"May I personally thank you and your team for the recent works completed our Project. What started<br>out to be a relatively straight forward project soon became problematic with its daily challenges!<br>However regular contact and communications with both Marco and the Site Supervisor Tom ensured that<br>the job was not only completed to plan but ahead of schedule as well!"</blockquote>
    <div class="who">Daniel Haroun,</div>
    <div class="where">Harbourvale North</div>
  </div>
  <div class="side-review right">"I have recommended<br>Construction &amp; Deve<br>many of my friends<br>work they have done<br>hesitate to recommend<br>future. We are very<br>work and especially<br>was left in an comple</div>
  <div class="arrow prev"><svg width="10" height="16" viewBox="0 0 10 16" fill="none" stroke="#fff" stroke-width="2.5"><path d="M8 2L2 8l6 6"/></svg></div>
  <div class="arrow next"><svg width="10" height="16" viewBox="0 0 10 16" fill="none" stroke="#fff" stroke-width="2.5"><path d="M2 2l6 6-6 6"/></svg></div>
</section>

<section class="contact">
  <h2 class="abs center">CONTACT US</h2>
  <div class="field" style="left:319px;top:134px;width:273px;height:44px">Name</div>
  <div class="field" style="left:607px;top:134px;width:274px;height:44px">Email</div>
  <div class="field" style="left:319px;top:191px;width:273px;height:44px">Phone</div>
  <div class="field select" style="left:607px;top:191px;width:274px;height:44px">Inquiry for</div>
  <div class="field" style="left:319px;top:250px;width:562px;height:144px">Message here....</div>
  <div class="btn">Send a message</div>
</section>

<footer class="site-footer">
  <div class="brand"><span>RW Construct</span><span class="dot"></span></div>
  <div class="chip" style="left:433px;width:196px">
    <span class="ico"><svg width="20" height="20" viewBox="0 0 24 24" fill="none" stroke="#fff" stroke-width="2"><path d="M5 3h4l2 5-2.5 1.5a11 11 0 0 0 6 6L16 13l5 2v4a2 2 0 0 1-2 2A17 17 0 0 1 3 5a2 2 0 0 1 2-2z"/></svg></span>+61 2 5550 0142
  </div>
  <div class="chip" style="left:640px;width:255px">
    <span class="ico"><svg width="20" height="20" viewBox="0 0 24 24" fill="none" stroke="#fff" stroke-width="2"><rect x="3" y="5" width="18" height="14"/><path d="M3 6l9 7 9-7"/></svg></span>info@rwbuildgroup.com.au
  </div>
  <div class="social" style="left:904px" aria-label="Social link"><span></span></div>
  <div class="social" style="left:950px" aria-label="Social link"><span></span></div>
  <div class="social" style="left:996px" aria-label="Social link"><span></span></div>
  <div class="rule"></div>
  <nav class="foot-links"><span>Home</span><span>About Us</span><span>Services</span><span>Projects</span><span>Contact Us</span></nav>
  <div class="copyright">Copyright © 2022 RW Construct | All Rights Reserved</div>
</footer>

</body>
</html>
```